E-Waste Recycling Company Business Card

New Electronic Recycling Company based in Long Island, New York called "Baron Rustwell" We take outdated computers, components, electrical wire, circuit breakers, ink cartridges, etc. We look mostly for donated items that we recycle for our customers but will pay for large quantities from businesses. The design should reflect that we are environmentally friendly and our unique Quadra Purge process that ensures all personal data is wiped clean off hard drives. Please use our attached logo
Electrical

```html
<!DOCTYPE html>
<html lang="en">
<head>
<meta charset="utf-8">
<title>Baron Rustwell – Business Card</title>
<link rel="stylesheet" href="https://fonts.googleapis.com/css2?family=Metamorphous&display=swap">
<style>
  :root {
    --border-green: #6f9a4e;
    --border-green-dark: #4f7a34;
    --panel-light: #e4f53a;
    --panel-mid: #a9de1f;
    --panel-deep: #5cbd1c;
    --disc-grey: #454a45;
    --disc-grey-dark: #353935;
    --ink-white: #f4f7ee;
    --ink-outline: #2f5a14;
    --emblem-tone: rgba(60, 120, 30, 0.35);
  }
  html, body {
    margin: 0;
    padding: 0;
    overflow: hidden;
    background: #ffffff;
  }
  .card {
    position: relative;
    width: 1200px;
    height: 720px;
    overflow: hidden;
    background:
      radial-gradient(circle at 20% 30%, rgba(255,255,255,0.12), transparent 40%),
      radial-gradient(circle at 80% 75%, rgba(0,0,0,0.12), transparent 45%),
      linear-gradient(135deg, var(--border-green), var(--border-green-dark));
    font-family: "Metamorphous", fantasy;
  }
  .card__panel {
    position: absolute;
    left: 40px;
    top: 40px;
    width: 1117px;
    height: 640px;
    overflow: hidden;
    background: radial-gradient(ellipse at 38% 45%, var(--panel-light) 0%, var(--panel-mid) 45%, var(--panel-deep) 100%);
  }
  .card__disc {
    position: absolute;
    left: 485px;
    top: -27px;
    width: 724px;
    height: 724px;
    border-radius: 50%;
    background: radial-gradient(circle at 45% 45%, var(--disc-grey) 0%, var(--disc-grey-dark) 100%);
  }
  .card__emblem-area {
    position: absolute;
    left: 3px;
    top: 3px;
    width: 234px;
    height: 298px;
    border-radius: 40% 50% 50% 40%;
    background: radial-gradient(ellipse at center, var(--emblem-tone), transparent 72%);
  }
  .brand__name,
  .brand__tagline,
  .offer__heading,
  .offer__list {
    color: var(--ink-white);
    -webkit-text-stroke: 1.2px var(--ink-outline);
    paint-order: stroke fill;
    margin: 0;
    position: absolute;
  }
  .brand__name {
    left: 4px;
    top: 8px;
    font-size: 52px;
    letter-spacing: 3px;
    font-variant: small-caps;
    line-height: 1;
  }
  .brand__tagline {
    left: 70px;
    top: 98px;
    width: 460px;
    text-align: center;
    font-size: 27px;
    font-variant: small-caps;
    -webkit-text-stroke: 1px var(--ink-outline);
  }
  .offer__heading {
    left: 4px;
    top: 318px;
    font-size: 50px;
    letter-spacing: 2px;
    font-variant: small-caps;
    line-height: 1;
  }
  .offer__list {
    left: 20px;
    top: 398px;
    width: 520px;
    list-style: none;
    padding: 0;
    text-align: center;
    font-size: 31px;
    line-height: 59px;
    font-variant: small-caps;
    -webkit-text-stroke: 1px var(--ink-outline);
  }
  .brand-mark {
    position: absolute;
    left: 620px;
    top: 260px;
    width: 480px;
    text-align: center;
    font-size: 56px;
    line-height: 1.15;
    color: var(--ink-white);
    font-variant: small-caps;
    margin: 0;
  }
</style>
</head>
<body>
  <main class="card">
    <section class="card__panel">
      <div class="card__disc"></div>
      <div class="card__emblem-area" role="img" aria-label="Faint recycling emblem with footprints"></div>

      <h1 class="brand__name">Baron Rustwell</h1>
      <p class="brand__tagline">Recycling And Waste Management</p>

      <h2 class="offer__heading">We Buy:-</h2>
      <ul class="offer__list">
        <li>Wires, Circuit Breakers,</li>
        <li>Outdated Laptops And Computers,</li>
        <li>Electric Motors And</li>
        <li>Other E-Waste</li>
      </ul>

      <p class="brand-mark">Baron<br>Rustwell</p>
    </section>
  </main>
</body>
</html>
```